quorVale - website to pay membership association fee

The main purpose of this site it to allow a pre-registered user to be able to view the membership fees for their membership association and pay the same in one of the ways offered by the portal.
You are required to create a graphical project only for the logon functions as a user, while omitting the back end/administration ones that will be decided later
The site, besides being responsive must be very intuitive in its function. The graphics must be bright.

Number of Pages Required

4 page

Requirements
Must have
• i need to see template for
• 1. Home page
• 2. Page after login. People can se one or more bill to Pay and decide to see more details or to pay.
• 3. Page to Pay. Choose the desired payment method five alternative

```html
<!DOCTYPE html>
<html lang="en">
<head>
<meta charset="utf-8">
<title>quorVale – Log In</title>
<link rel="stylesheet" href="https://fonts.googleapis.com/css2?family=Roboto:wght@300;400;500&family=Roboto+Condensed:wght@300;400&display=swap">
<style>
  :root {
    --blue: #0580d7;
    --blue-deep: #1a6fb0;
    --field-bg: #e9edf3;
    --field-border: #c9d1de;
    --placeholder: #8e9ab0;
    --icon: #7d8799;
    --title: #3a4a63;
    --muted: #7a8597;
    --link-purple: #7b3fa0;
    --white: #ffffff;
  }
  * { box-sizing: border-box; margin: 0; padding: 0; }
  html, body { width: 1200px; height: 750px; overflow: hidden; background: var(--white); }
  body { position: relative; font-family: "Roboto", Arial, sans-serif; font-weight: 300; }
  h1, h2 { font-weight: 400; }

  .hero {
    position: absolute; left: 23px; top: 25px; width: 347px; height: 193px;
    color: var(--white); overflow: hidden;
  }
  .hero-photo {
    position: absolute; inset: 0;
    background: radial-gradient(ellipse at 48% 45%, #2d6fa3 0%, var(--blue-deep) 45%, #1f79c2 100%);
  }
  .hero-links {
    position: absolute; top: 26px; left: 27px; right: 4px;
    display: flex; justify-content: space-between; font-size: 11.5px; font-weight: 400;
  }
  .hero-link { display: flex; align-items: center; gap: 6px; }
  .hero-title {
    position: absolute; left: 0; right: 0; top: 82px; text-align: center;
    font-family: "Roboto Condensed", Arial Narrow, sans-serif; font-weight: 400; line-height: 1;
  }
  .hero-title .big { font-size: 32px; display: block; }
  .hero-title .small { font-size: 20px; display: block; margin-top: 4px; }

  .field {
    position: absolute; height: 42px; background: var(--field-bg);
    border: 1px solid var(--field-border); border-radius: 3px;
    display: flex; align-items: center; font-size: 14px; color: var(--placeholder);
  }
  .field svg { flex: none; }
  .field.icon-right { justify-content: space-between; padding: 0 14px; }
  .field.icon-left { padding: 0 14px 0 16px; gap: 12px; }
  .field.plain { padding-left: 43px; }
  .field.select { padding: 0 12px 0 43px; justify-content: space-between; }

  .button {
    position: absolute; height: 43px; background: var(--blue); color: var(--white);
    border-radius: 3px; display: flex; align-items: center; justify-content: center;
    font-size: 14.5px; font-weight: 500;
  }
  .small-link { position: absolute; color: var(--blue); font-size: 11px; font-weight: 400; }

  .panel-title {
    position: absolute; left: 425px; top: 58px;
    font-family: "Roboto Condensed", Arial Narrow, sans-serif; font-weight: 400;
    font-size: 24px; color: var(--title);
  }
  .panel-sub { position: absolute; left: 426px; top: 95px; font-size: 13px; color: var(--muted); }
  .close { position: absolute; left: 1072px; top: 51px; }

  .agree {
    position: absolute; left: 431px; top: 279px; display: flex; align-items: center; gap: 9px;
    font-size: 14px; color: var(--muted);
  }
  .checkbox {
    width: 24px; height: 24px; background: var(--field-bg); border: 1px solid var(--field-border);
    border-radius: 3px; display: flex; align-items: center; justify-content: center;
  }
  .agree a { color: var(--link-purple); text-decoration: underline; }
</style>
</head>
<body>
  <section class="hero">
    <div class="hero-photo" role="img" aria-label="Blue-tinted photo of a vintage twin-lens camera on a table"></div>
    <div class="hero-links">
      <span class="hero-link">
        <svg width="19" height="16" viewBox="0 0 19 16"><circle cx="7" cy="5" r="4" fill="#fff"/><path d="M0 15c0-4 3-6 7-6s7 2 7 6z" fill="#fff"/><circle cx="14" cy="11" r="4.2" fill="#fff"/><path d="M14 8.8v4.4M11.8 11h4.4" stroke="#1a6fb0" stroke-width="1.4"/></svg>
        Request for Credentials
      </span>
      <span class="hero-link">
        <svg width="12" height="12" viewBox="0 0 12 12"><circle cx="6" cy="6" r="5" fill="#fff"/></svg>
        Request Assistance
      </span>
    </div>
    <h1 class="hero-title"><span class="big">LOG IN</span><span class="small">TO YOUR ACCOUNT</span></h1>
  </section>

  <div class="field icon-right" style="left:51px;top:247px;width:291px;">
    Username or Email
    <svg width="16" height="12" viewBox="0 0 16 12"><rect x="1" y="1" width="14" height="10" fill="none" stroke="var(--icon)" stroke-width="1.6"/><path d="M1 1l7 5 7-5" fill="none" stroke="var(--icon)" stroke-width="1.6"/></svg>
  </div>
  <div class="field icon-right" style="left:51px;top:303px;width:291px;">
    Password
    <svg width="13" height="16" viewBox="0 0 13 16"><path d="M3 7V5a3.5 3.5 0 017 0v2" fill="none" stroke="var(--icon)" stroke-width="1.8"/><rect x="1" y="7" width="11" height="8.5" rx="1" fill="var(--icon)"/></svg>
  </div>
  <div class="button" style="left:51px;top:368px;width:290px;">LOG IN</div>
  <a class="small-link" style="left:150px;top:412px;">Forgot Password?</a>
  <a class="small-link" style="left:173px;top:428px;">About Us</a>

  <h2 class="panel-title">CREATE CREDENTIALS</h2>
  <p class="panel-sub">Fill up all of the required fields</p>
  <svg class="close" width="13" height="13" viewBox="0 0 13 13"><path d="M1 1l11 11M12 1L1 12" stroke="var(--icon)" stroke-width="1.8"/></svg>

  <div class="field icon-left" style="left:426px;top:160px;width:296px;">
    <svg width="16" height="12" viewBox="0 0 16 12"><rect x="1" y="1" width="14" height="10" fill="none" stroke="var(--icon)" stroke-width="1.6"/><path d="M1 1l7 5 7-5" fill="none" stroke="var(--icon)" stroke-width="1.6"/></svg>
    Email
  </div>
  <div class="field icon-left" style="left:426px;top:217px;width:296px;">
    <svg width="13" height="16" viewBox="0 0 13 16"><path d="M3 7V5a3.5 3.5 0 017 0v2" fill="none" stroke="var(--icon)" stroke-width="1.8"/><rect x="1" y="7" width="11" height="8.5" rx="1" fill="var(--icon)"/></svg>
    Password
  </div>
  <div class="agree">
    <span class="checkbox"><svg width="14" height="11" viewBox="0 0 14 11"><path d="M1 5.5l4 4L13 1" fill="none" stroke="var(--icon)" stroke-width="1.8"/></svg></span>
    <span>I agree to the site's <a>Privacy Policy</a></span>
  </div>
  <a class="small-link" style="left:426px;top:381px;">Already Registered?</a>

  <div class="field select" style="left:761px;top:158px;width:298px;">
    Association Membership
    <svg width="12" height="8" viewBox="0 0 12 8"><path d="M1 1l5 5 5-5" fill="none" stroke="var(--icon)" stroke-width="1.6"/></svg>
  </div>
  <div class="field plain" style="left:762px;top:213px;width:297px;">Tax Identification Code</div>
  <div class="button" style="left:761px;top:268px;width:297px;">SUBMIT</div>
</body>
</html>
```